Food Hall in San Clemente, CA by the Pacific Ocean that has 15 vendors and 2 bars

We need a web page design that highlights our food hall in San Clemente, CA. The name of the food hall is Bellwick Food Hall. Inside of the food hall there are 15 different vendors and 2 bars. The place has a beautiful patio and it is by Pacific Ocean. Most of the vendors are local to San Clemente area. The highly anticipated location is opening during the summer of 2025. Website should have a dropdown menu for the different vendors that are in the food hall and people should be able to click to their respective business website. The website should also include link to our social media channels and also a link to provide comments and subscribe for the mailing list.
Target Market(s)
Mostly residents in the San Clemente, CA and surrounding areas. Couples, families and tourist alike that are looking for an exceptional dining experience that everyone can find something they like.
Industry/Entity Type
Restaurants
Coding
Coded - Design and coding required
Number of Pages Required
5+ page
Font styles to use
Look and feel

```html
<!DOCTYPE html>
<html lang="en">
<head>
<meta charset="UTF-8">
<title>Bellwick Food Hall – San Clemente</title>
<link rel="stylesheet" href="https://fonts.googleapis.com/css2?family=Poppins:wght@500;600;700&family=Inter:wght@400;500;600&display=swap">
<style>
  :root {
    --ink: #111111;
    --white: #ffffff;
    --accent: #7aa7d6;
    --accent-soft: #c7dbf0;
    --panel-grey: #ececec;
    --patio-grey: #d9d9d9;
    --border-grey: #d4d4d4;
    --hero-dark: #1d2126;
    --band-dark: #25272a;
    --footer-navy: #0e4b7c;
    --muted: #333333;
  }
  * { box-sizing: border-box; margin: 0; padding: 0; }
  html, body { width: 1200px; height: 4090px; overflow: hidden; background: var(--white); }
  body { position: relative; font-family: "Inter", sans-serif; color: var(--ink); }
  .abs { position: absolute; }
  .display { font-family: "Poppins", sans-serif; font-weight: 600; text-transform: uppercase; letter-spacing: 0.5px; }
  .center { text-align: center; }
  .btn {
    position: absolute; display: flex; align-items: center; justify-content: center;
    border-radius: 10px; font-family: "Inter", sans-serif; font-weight: 600; font-size: 14px;
    text-decoration: none;
  }
  .btn-accent { background: var(--accent); color: var(--white); }
  .btn-light { background: var(--white); color: var(--ink); }

  /* Hero */
  .hero { left: 0; top: 0; width: 1200px; height: 728px;
    background: linear-gradient(90deg, #050607 0%, #2b3036 45%, #5a5f63 75%, #7a7168 100%); }
  .nav-logo { left: 60px; top: 24px; color: var(--white); font-family: "Poppins", sans-serif; font-weight: 600; font-size: 34px; }
  .nav-link { top: 32px; color: var(--white); font-size: 15px; text-decoration: none; }
  .hero-title { left: 60px; top: 196px; color: var(--white); font-size: 80px; line-height: 84px; font-weight: 600; }
  .hero-copy { left: 60px; top: 392px; width: 490px; color: var(--white); font-size: 15px; line-height: 25px; }

  /* Vendors */
  .section-title { left: 0; width: 1200px; font-size: 44px; line-height: 52px; }
  .section-sub { left: 0; width: 1200px; font-size: 15px; }
  .vendor-card { top: 949px; width: 352px; height: 395px; border-radius: 18px; border: 3px solid var(--border-grey); background: var(--white); }
  .vendor-card.is-featured { background: var(--accent-soft); border-color: var(--accent-soft); }
  .vendor-photo { position: absolute; left: 10px; top: 22px; width: 326px; height: 230px; border-radius: 14px; }
  .vendor-name { position: absolute; left: 0; width: 100%; top: 278px; text-align: center; font-family: "Poppins", sans-serif; font-weight: 600; font-size: 22px; }
  .vendor-desc { position: absolute; left: 30px; right: 30px; top: 318px; text-align: center; font-size: 14px; line-height: 24px; }

  /* Taste band */
  .taste { left: 0; top: 1508px; width: 1200px; height: 397px;
    background: linear-gradient(90deg, #2e3032 0%, #1c1d1f 50%, #2a2c2e 100%); }

  /* Bars */
  .bar-photo { border-radius: 18px; }
  .bar-frame { left: 273px; top: 2281px; width: 292px; height: 391px; background: var(--white); border-radius: 20px; }
  .bar-card { width: 259px; border-radius: 14px; background: var(--panel-grey); text-align: center; }
  .bar-card.is-featured { background: var(--accent-soft); }
  .bar-card h3 { font-family: "Poppins", sans-serif; font-weight: 600; font-size: 18px; margin-top: 30px; }
  .bar-card p { font-size: 14px; line-height: 24px; margin: 10px 24px 0; }
  .bar-card .btn { position: relative; margin: 14px auto 0; width: 124px; height: 40px; }

  /* Patio */
  .patio-box { left: 60px; top: 2894px; width: 530px; height: 347px; background: var(--patio-grey); border: 2px solid #8a8a8a; border-radius: 18px; }
  .patio-photo { left: 610px; top: 2894px; width: 530px; height: 347px; border-radius: 18px;
    background: linear-gradient(180deg, #4a5e6e 0%, #7e8e98 45%, #9aa3a4 70%, #6d6458 100%); }
  .play { left: 837px; top: 3023px; width: 76px; height: 56px; background: var(--white); border-radius: 12px; }

  /* Contact */
  .field { background: var(--white); border-radius: 14px; box-shadow: 0 3px 3px rgba(0,0,0,0.22); border: 1px solid #eeeeee; font-size: 14px; padding: 14px 6px; }
  .map { left: 610px; top: 3332px; width: 530px; height: 414px; border-radius: 14px;
    background: linear-gradient(135deg, #e9dfc4 0%, #d8cfa8 40%, #b7d58c 60%, #e6dcc3 100%); }

  /* Footer */
  .footer { left: 0; top: 3838px; width: 1200px; height: 252px; background: var(--footer-navy); color: var(--white); }
  .footer a { color: var(--white); text-decoration: none; }
  .social { width: 28px; height: 28px; border: 2px solid var(--white); border-radius: 50%; }
</style>
</head>
<body>

<!-- Hero -->
<header class="abs hero" role="img" aria-label="Photo of the food hall dining room with chairs, tables and tall windows"></header>
<div class="abs nav-logo">LOGO</div>
<a class="abs nav-link" style="left:382px" href="#">Home</a>
<a class="abs nav-link" style="left:511px" href="#">Vendors
  <svg width="9" height="6" viewBox="0 0 9 6"><path d="M1 1l3.5 3.5L8 1" stroke="#fff" fill="none" stroke-width="1.4"/></svg></a>
<a class="abs nav-link" style="left:670px" href="#">Bar</a>
<a class="abs nav-link" style="left:779px" href="#">Patio</a>
<a class="btn btn-light" style="left:1020px;top:19px;width:120px;height:41px;" href="#">Contact</a>
<h1 class="abs display hero-title">Locally Made<br>Lovingly Shared</h1>
<p class="abs hero-copy">15 Local Vendors. 2 Vibrant Bars. Endless Flavors. Opening Summer 202515 Local Vendors. 2 Vibrant Bars. Endless Flavors. Opening Summer 2025..</p>
<a class="btn btn-light" style="left:60px;top:502px;width:143px;height:46px;" href="#">Discover More</a>

<!-- Vendors -->
<h2 class="abs display center section-title" style="top:826px">Meet Our Local Vendors</h2>
<p class="abs center section-sub" style="top:886px;font-size:14px;text-transform:uppercase;">Indulge in a variety of flavors, crafted by San Clemente’s finest local makers.</p>

<article class="abs vendor-card is-featured" style="left:60px">
  <div class="vendor-photo" role="img" aria-label="Pizza kitchen interior with wood counters and hanging lamps" style="background:linear-gradient(180deg,#5a3a24,#a8764a 60%,#d9c29a);"></div>
  <h3 class="vendor-name">PIZZA KITCHEN</h3>
  <p class="vendor-desc">Crafting Perfect Pizzas, One Slice At A Time – A Taste You’ll Love.</p>
</article>
<article class="abs vendor-card" style="left:424px">
  <div class="vendor-photo" role="img" aria-label="Skewers of meat grilling over smoke" style="background:linear-gradient(180deg,#2a4a6e,#6f88a0 40%,#5a2e1a 75%,#2a1a14);"></div>
  <h3 class="vendor-name">BBQ HAVEN</h3>
  <p class="vendor-desc">Smoky, Tender, And Full Of Flavor – Where Every Bite Feels Like Home.</p>
</article>
<article class="abs vendor-card" style="left:789px">
  <div class="vendor-photo" role="img" aria-label="Plate of creamy pasta with herbs" style="top:22px;height:222px;background:linear-gradient(180deg,#e8e2d6,#e2c07a 50%,#c9a45a);"></div>
  <h3 class="vendor-name" style="top:270px">PASTA PERFECTION</h3>
  <p class="vendor-desc">Authentic Italian Taste With An American Twist – Every Bowl Made To Satisfy.</p>
</article>
<a class="btn btn-accent" style="left:529px;top:1378px;width:142px;height:47px;" href="#">Discover More</a>

<!-- Taste band -->
<section class="abs taste" role="img" aria-label="Dim photo of the food hall market aisles and seating"></section>
<h2 class="abs display center section-title" style="top:1606px;color:var(--white);font-size:42px;">A Taste Of San Clemente</h2>
<p class="abs center" style="left:240px;top:1668px;width:720px;color:var(--white);font-size:15px;line-height:25px;">• At Bellwick Food Hall, Every Craving Finds Its Match, Whether You’re In The Mood For Something Bold, Fresh, Sweet, Or Savory.</p>
<a class="btn btn-accent" style="left:529px;top:1754px;width:142px;height:46px;" href="#">Discover More</a>

<!-- Bars -->
<h2 class="abs display center section-title" style="top:2004px">Stylish Full-Service Bars</h2>
<p class="abs center" style="left:230px;top:2064px;width:740px;font-size:14px;line-height:19px;">experience handcrafted cocktails and chilled drinks in a vibrant atmosphere. whether you’re here for happy hour or a late-night toast, our bars have it all.</p>

<div class="abs bar-photo" style="left:60px;top:2146px;width:286px;height:373px;background:linear-gradient(180deg,#5a2a1c,#b8641c 50%,#e3a040);" role="img" aria-label="Frothy mug of amber beer"></div>
<div class="abs bar-frame"></div>
<div class="abs bar-photo" style="left:286px;top:2297px;width:273px;height:375px;border-radius:14px;background:linear-gradient(180deg,#c8c4bc,#7a766e 50%,#2a2826 80%,#c9c5bd);" role="img" aria-label="Bartender pouring a drink over ice"></div>

<div class="abs bar-card is-featured" style="left:608px;top:2244px;height:194px;">
  <h3>Signature Cocktails</h3>
  <p>From Classics To Creative— Sip Something Special</p>
  <a class="btn btn-accent" href="#">Learn More</a>
</div>
<div class="abs bar-card" style="left:608px;top:2456px;height:193px;">
  <h3>Wine</h3>
  <p>Bold Reds, Bright Whites, And Beachside Nights</p>
  <a class="btn btn-accent" href="#">Learn More</a>
</div>
<div class="abs bar-card" style="left:883px;top:2175px;height:185px;">
  <h3>Beers</h3>
  <p>Pouring Local Flavor, One Pint At A Time</p>
  <a class="btn btn-accent" href="#">Learn More</a>
</div>
<div class="abs bar-card" style="left:883px;top:2376px;height:187px;">
  <h3>Non-Alcoholic</h3>
  <p>Mocktails That Make A Statement</p>
  <a class="btn btn-accent" href="#">Learn More</a>
</div>

<!-- Patio -->
<h2 class="abs display center section-title" style="top:2771px">Coastal Dining, Open Air Style</h2>
<p class="abs center section-sub" style="top:2831px;font-size:14px;">Soak Up The Sun, Savor Every Bite, And Feel The Ocean Breeze.</p>

<div class="abs patio-box"></div>
<h3 class="abs" style="left:94px;top:2950px;width:480px;font-family:'Poppins',sans-serif;font-weight:500;font-size:35px;line-height:38px;">Dine Under The Sky, Steps From The Sea</h3>
<p class="abs" style="left:94px;top:3040px;width:480px;font-size:14px;line-height:24px;color:var(--muted);">Enjoy Open-Air Seating With Fresh Ocean Breeze, Sunshine, And. Our Spacious Patio Is Perfect For Family Meals, Date Nights, Soak In The San Clemente Charm – Day Or Night.</p>
<a class="btn btn-accent" style="left:98px;top:3132px;width:143px;height:51px;" href="#">Discover More</a>

<div class="abs patio-photo" role="img" aria-label="Video still of a couple dining at a table by the water under hanging lights"></div>
<div class="abs play">
  <svg width="76" height="56" viewBox="0 0 76 56"><path d="M46 17v22L28 28z" fill="#000"/></svg>
</div>

<!-- Contact -->
<h2 class="abs display" style="left:63px;top:3338px;font-size:44px;line-height:52px;">Contact Us</h2>
<div class="abs field" style="left:60px;top:3416px;width:254px;height:41px;padding-top:12px;">Name :</div>
<div class="abs field" style="left:333px;top:3416px;width:257px;height:41px;padding-top:10px;">Email :</div>
<div class="abs field" style="left:60px;top:3475px;width:530px;height:41px;padding-top:12px;">Subject :</div>
<div class="abs field" style="left:60px;top:3530px;width:530px;height:138px;padding-top:14px;">Message :</div>
<a class="btn btn-accent" style="left:60px;top:3695px;width:530px;height:51px;font-weight:500;" href="#">Subment Button</a>
<div class="abs map" role="img" aria-label="Street map showing the food hall location with a river and parks"></div>
<svg class="abs" style="left:864px;top:3520px" width="24" height="34" viewBox="0 0 24 34" aria-hidden="true">
  <path d="M12 33C12 33 2 19 2 12a10 10 0 0 1 20 0c0 7-10 21-10 21z" fill="#d0211c"/>
  <circle cx="12" cy="12" r="3.5" fill="#8a1210"/>
</svg>

<!-- Footer -->
<footer class="abs footer">
  <div class="abs display" style="left:60px;top:50px;font-size:44px;line-height:52px;">San Clemente</div>
  <nav>
    <a class="abs" style="left:60px;top:128px;font-size:15px;" href="#">home</a>
    <a class="abs" style="left:165px;top:128px;font-size:15px;" href="#">vendors</a>
    <a class="abs" style="left:286px;top:128px;font-size:15px;" href="#">event</a>
    <a class="abs" style="left:389px;top:128px;font-size:15px;" href="#">patio</a>
    <a class="abs" style="left:468px;top:128px;font-size:15px;" href="#">contact</a>
  </nav>
  <p class="abs" style="left:844px;top:46px;width:300px;font-size:14px;line-height:24px;">Stay Updated With The Latest Flavors And Events At Bellwick Food Hall.</p>
  <a class="abs social" style="left:843px;top:121px;" href="#" aria-label="Social channel"></a>
  <a class="abs social" style="left:888px;top:121px;" href="#" aria-label="Social channel"></a>
  <a class="abs social" style="left:934px;top:121px;" href="#" aria-label="Social channel"></a>
  <a class="abs social" style="left:978px;top:121px;" href="#" aria-label="Social channel"></a>
  <div class="abs" style="left:60px;top:186px;width:1080px;height:2px;background:var(--white);"></div>
  <p class="abs" style="left:60px;top:215px;font-size:11px;">Copyright © 2025 All Right Reserved</p>
  <a class="abs" style="left:817px;top:215px;font-size:11px;" href="#">Privacy Policy</a>
  <a class="abs" style="left:924px;top:215px;font-size:11px;" href="#">Terms Of Service</a>
  <a class="abs" style="left:1048px;top:215px;font-size:11px;" href="#">Cookies Settings</a>
</footer>

</body>
</html>
```